AUTOMOTIVE/ CAR REPAIRS / CRASH REPAIRS / PAINT SPRAYING AND PANEL BEATING

AUTOMOTIVE REPAIR. CAR / MOTORCYCLES GOT LOGO DESIGN / DID THINK ABOUT FACEBOOK DONT NOALREADY HAVE WEB ADRESS www.brentavel.co.uk and mail sales@brentavel,co.uk NEED SOMETHINK I CAN MANAGE TO UPLOAD PICTURES IN TO A GALLERY OR SOMETHINGLIKE THAT I ALSO SELL CAR AND MOTORCYCLES MAYBE A SELLS PAGE WITH A QUIDLOOP LINK

Target Market(s)

TRADE / GENERAL PUBLIC

Industry/Entity Type

Automotive

Coding

Coded - Design and coding required

Number of Pages Required

4 page

Font styles to use
Serif
Sans Serif

Colors

Designer to choose colors to be used in the design.

Requirements
Must have
• GALLERY/ SHOP TO SALE CARS AND MOTORCYCLE / LOGOS OF MATERIALS I USE TORVENDE / KELP / SANVITE / Q BAND / GLIDECARE
• CONTACT US
Nice to have
• QUIDLOOP / EASY TO MANAGE / VIDEO CLIP OF TORVENDE TINT PLANNER Q7
• SWIFT BLEND PAINT LUMINEL HYDROLUX AND PELOVAN

```html
<!DOCTYPE html>
<html lang="en">
<head>
<meta charset="utf-8">
<title>Brentavel Bodyshop</title>
<link href="https://fonts.googleapis.com/css2?family=Roboto:wght@400;500;700&family=Open+Sans:wght@400;600&display=swap" rel="stylesheet">
<style>
:root{
  --red:#c4111b;
  --red-dark:#8e0a12;
  --ink:#1b1b1b;
  --text:#333;
  --grey:#d9d9d9;
  --light:#f2f2f2;
  --night:#1d1d1d;
  --white:#fff;
}
*{margin:0;padding:0;box-sizing:border-box}
html,body{width:1200px;height:4515px;overflow:hidden}
body{position:relative;background:var(--white);font-family:"Open Sans",Arial,sans-serif;color:var(--text)}
.abs{position:absolute}
.head-font{font-family:"Roboto",Arial,sans-serif}
/* hero */
.hero{left:0;top:0;width:1200px;height:736px;background:linear-gradient(120deg,#2a2a2a 0%,#5a5a5a 40%,#8c8c8c 62%,#3b3b3b 100%)}
.brand{left:79px;top:30px;font-family:"Roboto",Arial,sans-serif;color:var(--white);font-weight:700;font-size:38px;letter-spacing:4px}
.brand small{display:block;font-size:15px;font-weight:400;letter-spacing:12px;margin:6px 0 0 70px}
.nav{left:422px;top:54px;display:flex;gap:0;font-family:"Roboto",Arial,sans-serif;font-weight:500;font-size:17px;color:var(--white)}
.nav span{margin-right:35px}
.nav .active{color:var(--red)}
.nav-phone{left:985px;top:50px;color:var(--white);font-family:"Roboto",Arial,sans-serif;font-weight:500;font-size:19px;display:flex;align-items:center;gap:6px}
.hero-title{left:0;width:755px;top:256px;text-align:center;font-family:"Roboto",Arial,sans-serif;font-weight:700;color:var(--white);font-size:52px;line-height:52px}
.hero-title .second{color:#d8d8d8}
.hero-tag{left:0;width:755px;top:372px;text-align:center;font-family:"Roboto",Arial,sans-serif;font-weight:500;color:var(--white);font-size:24px}
.btn-red{background:var(--red);color:var(--white);font-family:"Roboto",Arial,sans-serif;font-weight:500;font-size:17px;display:flex;align-items:center;justify-content:center}
.hero-btn{left:289px;top:420px;width:175px;height:48px}
/* about */
.about-bg{left:0;top:700px;width:1200px;height:500px;background:linear-gradient(#e4e4e4,#fff)}
.about-mark{left:193px;top:790px;width:306px;height:306px;border-radius:50%;background:radial-gradient(circle at 40% 35%,#fff 0%,#e6e6e6 55%,#c9c9c9 100%);display:flex;align-items:center;justify-content:center;font-family:"Roboto",Arial,sans-serif;font-weight:700;font-size:40px;color:var(--red)}
.about-title{left:564px;top:780px;font-family:"Roboto",Arial,sans-serif;font-weight:500;font-size:35px;color:var(--ink)}
.about-text{left:564px;top:838px;width:490px;font-size:18px;line-height:31px;color:#444}
.btn-outline{border:2px solid var(--red);color:var(--red);font-family:"Roboto",Arial,sans-serif;font-weight:500;font-size:17px;display:flex;align-items:center;justify-content:center;background:var(--white)}
.about-btn{left:564px;top:1018px;width:177px;height:51px}
/* services */
.sec-title{left:0;width:1200px;text-align:center;font-family:"Roboto",Arial,sans-serif;font-weight:500;font-size:34px;color:var(--ink)}
.sec-title.red{color:var(--red);font-weight:700}
.tile{top:1312px;height:274px;display:flex;align-items:flex-end;justify-content:center;padding-bottom:26px;color:var(--white);font-family:"Roboto",Arial,sans-serif;font-weight:500;font-size:20px}
.tile-1{left:0;width:294px;background:linear-gradient(160deg,#3a3a3a,#8a8a8a 50%,#2a2a2a)}
.tile-2{left:301px;width:295px;background:linear-gradient(150deg,#6d6d6d,#2b4fa0 60%,#1a2a55)}
.tile-4{left:906px;width:294px;background:linear-gradient(160deg,#6a6a6a,#9a9a9a 45%,#2d2d2d)}
.tile-3{left:604px;top:1288px;width:295px;height:319px;background:radial-gradient(circle at 50% 45%,#d3232b,#a50d16 70%,#8a0a12);flex-direction:column;justify-content:center;align-items:center;padding:0 26px;text-align:center}
.tile-3 h3{font-weight:500;font-size:22px;margin-bottom:12px}
.tile-3 p{font-family:"Open Sans",Arial,sans-serif;font-size:13px;line-height:18px}
.tile-3 .chev{margin-top:14px;width:36px;height:36px;border-radius:50%;background:var(--white);display:flex;align-items:center;justify-content:center}
/* why */
.why-car{left:657px;top:1690px;width:543px;height:465px;background:radial-gradient(ellipse at 55% 55%,#e6e6e6 0%,#b5b5b5 45%,rgba(255,255,255,0) 72%)}
.why-item{left:168px;display:flex;gap:10px}
.why-item .txt h4{font-family:"Roboto",Arial,sans-serif;font-weight:500;color:var(--red);font-size:16px;margin-bottom:6px}
.why-item .txt p{font-size:13px;line-height:19px;color:#333;width:385px}
/* gallery */
.gallery-bg{left:0;top:2240px;width:1200px;height:670px;background:linear-gradient(#cfcfcf,#f4f4f4 70%)}
.ph{position:absolute}
.brands{left:0;top:2800px;width:1200px;height:60px}
.brand-name{position:absolute;top:12px;font-family:"Roboto",Arial,sans-serif;font-weight:700;font-size:26px;color:#222;display:flex;align-items:center;gap:8px}
.brand-name i{display:inline-block;width:16px;height:16px;border-radius:50%;background:var(--red)}
/* products */
.products{left:0;top:2908px;width:1200px;height:386px;background:linear-gradient(90deg,#6e0a10,#a0121b 50%,#6e0a10)}
.products h2{position:absolute;left:0;width:1212px;top:102px;text-align:center;font-family:"Roboto",Arial,sans-serif;font-weight:500;font-size:34px;color:var(--white)}
.products p{position:absolute;left:220px;width:770px;top:150px;text-align:center;font-size:19px;line-height:31px;color:#f1d6d7}
.btn-ghost{border:2px solid var(--white);color:var(--white);font-family:"Roboto",Arial,sans-serif;font-weight:500;font-size:17px;display:flex;align-items:center;justify-content:center}
.products .btn-ghost{position:absolute;left:517px;top:237px;width:177px;height:49px}
/* contact */
.contact{left:0;top:3294px;width:1200px;height:560px;background:var(--night)}
.contact h2{position:absolute;left:0;width:1212px;top:46px;text-align:center;font-family:"Roboto",Arial,sans-serif;font-weight:500;font-size:34px;color:var(--white)}
.c-item{position:absolute;top:126px;width:340px;text-align:center;color:var(--white)}
.c-item svg{display:block;margin:0 auto}
.c-item h5{font-family:"Roboto",Arial,sans-serif;font-weight:500;font-size:18px;margin-top:18px}
.c-item p{font-size:17px;line-height:31px;color:#ddd}
/* appointment */
.appt-title{left:0;width:1194px;top:3858px;text-align:center;font-family:"Roboto",Arial,sans-serif;font-weight:500;font-size:31px;color:var(--red)}
.appt-addr{left:0;width:1200px;top:3900px;text-align:center;font-family:"Roboto",Arial,sans-serif;font-size:17px;line-height:31px;color:#444}
.field{border:1px solid #9a9a9a;height:51px;padding-left:20px;display:flex;align-items:center;font-family:"Roboto",Arial,sans-serif;font-size:17px;color:#444;background:var(--white)}
.appt-note{left:0;width:1200px;top:4140px;text-align:center;font-family:"Roboto",Arial,sans-serif;font-size:19px;line-height:27px;color:#444}
/* footer */
.footer-bg{left:0;top:4300px;width:1200px;height:215px;background:var(--night)}
.foot-nav{left:161px;top:4405px;display:flex;font-family:"Roboto",Arial,sans-serif;font-weight:500;font-size:17px;color:var(--white)}
.foot-nav span{margin-right:34px}
.copy{left:161px;top:4444px;font-size:13px;color:#ccc}
.social{top:4404px;width:28px;height:28px;border-radius:50%;background:#bdbdbd}
.pay{left:995px;top:4402px;font-family:"Roboto",Arial,sans-serif;font-weight:700;font-size:22px;color:var(--white)}
</style>
</head>
<body>

<!-- hero -->
<div class="abs hero" role="img" aria-label="Photo of a silver convertible sports car in the workshop"></div>
<div class="abs brand">BRENTAVEL<small>BODYSHOP</small></div>
<nav class="abs nav"><span class="active">ABOUT US</span><span>SERVICE</span><span>CUSTOM</span><span>GALLERY</span><span>CONTACT</span></nav>
<div class="abs nav-phone">
  <svg width="18" height="18" viewBox="0 0 24 24"><path d="M6.6 10.8a15 15 0 0 0 6.6 6.6l2.2-2.2a1 1 0 0 1 1-.25 11.4 11.4 0 0 0 3.6.57 1 1 0 0 1 1 1V20a1 1 0 0 1-1 1A17 17 0 0 1 3 4a1 1 0 0 1 1-1h3.5a1 1 0 0 1 1 1c0 1.25.2 2.45.57 3.57a1 1 0 0 1-.25 1z" fill="#fff"/></svg>
  0771 555 0192
</div>
<div class="abs hero-title">YOUR ONE STOP<br><span class="second">BODY SHOP</span></div>
<div class="abs hero-tag">THE HOME OF PAINT PERFECTION</div>
<div class="abs btn-red hero-btn">CONTACT US</div>
<svg class="abs" style="left:84px;top:305px" width="32" height="60" viewBox="0 0 32 60"><path d="M28 2 4 30l24 28" fill="none" stroke="#fff" stroke-width="3"/></svg>
<svg class="abs" style="left:1082px;top:305px" width="32" height="60" viewBox="0 0 32 60"><path d="M4 2l24 28L4 58" fill="none" stroke="#fff" stroke-width="3"/></svg>

<!-- about -->
<div class="abs about-bg"></div>
<svg class="abs" style="left:0;top:590px" width="1200" height="150" viewBox="0 0 1200 150">
  <path d="M0 150 L0 135 C300 150 700 70 1200 60 L1200 150 Z" fill="#e4e4e4"/>
  <path d="M377 122 C650 55 950 5 1200 25 L1200 115 C1000 60 700 80 377 122 Z" fill="var(--red)"/>
</svg>
<div class="abs about-mark">BRENTAVEL</div>
<h2 class="abs about-title">BRENTAVEL BODYSHOP</h2>
<p class="abs about-text">Brentavel, based in Elmsworth, Derbyshire established in August, 1985 has grown to become Derbyshire's premiere manufacturer approved accident repair centre. Equipped with the latest technology and factory trained technicians, we process accident repairs</p>
<div class="abs btn-outline about-btn">READ MORE</div>

<!-- what we do -->
<h2 class="abs sec-title red" style="top:1204px">WHAT WE DO</h2>
<div class="abs tile tile-1" role="img" aria-label="Photo of a car body panel being repaired">CAR BODY REPAIRS</div>
<div class="abs tile tile-2" role="img" aria-label="Photo of a motorcycle part being spray painted">MOTORCYCLE PAINTING</div>
<div class="abs tile tile-3">
  <h3>WHEEL PAINTING</h3>
  <p>ullamcorper est eget tempor cursus neque mi consectetuer mi a ultricies massa est sed nisl Class aptent taciti sociosqu ad litora</p>
  <div class="chev"><svg width="16" height="10" viewBox="0 0 16 10"><path d="M2 2l6 6 6-6" fill="none" stroke="#c4111b" stroke-width="2.5"/></svg></div>
</div>
<div class="abs tile tile-4" role="img" aria-label="Photo of a grey saloon car front">IE CARS AND BIKES</div>

<!-- why choose us -->
<h2 class="abs sec-title" style="top:1656px">WHY CHOOSE US</h2>
<div class="abs why-car" role="img" aria-label="Silver saloon car in side view"></div>
<svg class="abs" style="left:0;top:1700px" width="1200" height="400" viewBox="0 1700 1200 400">
  <g fill="none" stroke="#777" stroke-width="1.2">
    <polyline points="426,1756 728,1756 820,1827"/>
    <polyline points="440,1843 662,1843 743,1896"/>
    <polyline points="338,1953 617,1953 652,1976"/>
    <polyline points="455,2067 643,2067"/>
  </g>
  <g fill="var(--red)">
    <circle cx="820" cy="1829" r="6"/><circle cx="743" cy="1896" r="6"/>
    <circle cx="652" cy="1976" r="5"/><circle cx="645" cy="2067" r="5"/>
  </g>
</svg>
<div class="abs why-item" style="top:1744px">
  <svg width="30" height="30" viewBox="0 0 30 30"><circle cx="15" cy="15" r="13" fill="none" stroke="#c4111b" stroke-width="2"/><path d="M8 15l5 5 9-10" fill="none" stroke="#c4111b" stroke-width="2.2"/></svg>
  <div class="txt"><h4>FULL OR PART RESPRAYS</h4><p>Single panel resprays to full car resprays</p></div>
</div>
<div class="abs why-item" style="top:1831px">
  <svg width="30" height="30" viewBox="0 0 30 30"><circle cx="15" cy="15" r="13" fill="none" stroke="#c4111b" stroke-width="2"/><path d="M8 15l5 5 9-10" fill="none" stroke="#c4111b" stroke-width="2.2"/></svg>
  <div class="txt"><h4>DENT &amp; SCRATCH REMOVAL</h4><p>From small paintless dent repairs to full panel replacements. Scratches, chips &amp; paint repairs undertaken</p></div>
</div>
<div class="abs why-item" style="top:1941px">
  <svg width="30" height="30" viewBox="0 0 30 30"><circle cx="15" cy="15" r="13" fill="none" stroke="#c4111b" stroke-width="2"/><path d="M8 15l5 5 9-10" fill="none" stroke="#c4111b" stroke-width="2.2"/></svg>
  <div class="txt"><h4>BUMPER REPAIR</h4><p>Bumper scuffs, plastic bumper repairs and full bumper replacements. Full factory matched colours.</p></div>
</div>
<div class="abs why-item" style="top:2055px">
  <svg width="30" height="30" viewBox="0 0 30 30"><circle cx="15" cy="15" r="13" fill="none" stroke="#c4111b" stroke-width="2"/><path d="M8 15l5 5 9-10" fill="none" stroke="#c4111b" stroke-width="2.2"/></svg>
  <div class="txt"><h4>ALLOY WHEEL'S REFURBISHED</h4><p>All accident repair undertaken. Just one call to Brentavel and we'll help you take the first steps towards getting</p></div>
</div>

<!-- gallery -->
<div class="abs gallery-bg"></div>
<svg class="abs" style="left:0;top:2170px" width="1200" height="120" viewBox="0 0 1200 120">
  <path d="M0 120 L0 80 C300 90 600 55 840 20 C600 90 300 120 0 120 Z" fill="#cfcfcf"/>
  <path d="M0 45 C300 80 600 50 840 20 C600 75 300 115 0 108 Z" fill="var(--red)"/>
</svg>
<h2 class="abs sec-title" style="top:2304px">OUR GALLERY</h2>
<div class="ph" style="left:161px;top:2376px;width:333px;height:361px;background:linear-gradient(150deg,#8a8a8a,#c21a22 55%,#5a5a5a)" role="img" aria-label="Photo of a red classic car body stripped for repair"></div>
<div class="ph" style="left:506px;top:2376px;width:172px;height:173px;background:linear-gradient(150deg,#bcbcbc,#7a7a7a)" role="img" aria-label="Photo of a car bonnet masked for painting"></div>
<div class="ph" style="left:687px;top:2376px;width:352px;height:173px;background:linear-gradient(150deg,#6d6d6d,#a5a5a5 50%,#3b3b3b)" role="img" aria-label="Photo of a grey saloon front end in the workshop"></div>
<div class="ph" style="left:506px;top:2563px;width:172px;height:174px;background:linear-gradient(150deg,#9a9a9a,#7a2a30)" role="img" aria-label="Photo of a classic car interior with steering wheel"></div>
<div class="ph" style="left:687px;top:2563px;width:171px;height:174px;background:linear-gradient(150deg,#e6e6e6,#3a3a3a)" role="img" aria-label="Photo of a white hatchback front"></div>
<div class="ph" style="left:867px;top:2563px;width:172px;height:174px;background:linear-gradient(150deg,#2a2a2a,#5b6470)" role="img" aria-label="Photo of a dark car on the workshop floor"></div>
<div class="abs brands">
  <span class="brand-name" style="left:195px">TORVENDE</span>
  <span class="brand-name" style="left:432px">KELP</span>
  <span class="brand-name" style="left:573px">SANVITE</span>
  <span class="brand-name" style="left:740px">Q BAND</span>
  <span class="brand-name" style="left:880px"><i></i>GLIDECARE</span>
</div>

<!-- products -->
<section class="abs products" role="img" aria-label="Dark red tinted photo of a car interior">
  <h2>BUY OUR PRODUCTS</h2>
  <p>Allamcorper est eget tempor cursus neque mi consectetuer mi a ultricies massa est sed nisl Class aptent taciti sociosqu ad litora torquent per</p>
  <div class="btn-ghost">SHOP NOW</div>
</section>

<!-- contact -->
<section class="abs contact">
  <h2>CONTACT US</h2>
  <div class="c-item" style="left:137px">
    <svg width="150" height="150" viewBox="0 0 150 150"><path d="M20 90 A58 58 0 0 1 130 50 A52 52 0 0 0 20 90Z" fill="var(--red)"/><circle cx="80" cy="78" r="56" fill="#fff"/><circle cx="80" cy="78" r="44" fill="none" stroke="#e0e0e0" stroke-width="2"/><path d="M80 100s-16-17-16-28a16 16 0 0 1 32 0c0 11-16 28-16 28z" fill="none" stroke="#c4111b" stroke-width="3"/><circle cx="80" cy="72" r="6" fill="none" stroke="#c4111b" stroke-width="3"/></svg>
    <h5>OUR ADDRESS</h5>
    <p>Brentavel Bodyshop, Harrowgate<br>Trade Park, Copse Lane, Elmsworth,<br>Derbyshire, DE99 4ZQ</p>
  </div>
  <div class="c-item" style="left:427px">
    <svg width="150" height="150" viewBox="0 0 150 150"><path d="M20 90 A58 58 0 0 1 130 50 A52 52 0 0 0 20 90Z" fill="var(--red)"/><circle cx="80" cy="78" r="56" fill="#fff"/><circle cx="80" cy="78" r="44" fill="none" stroke="#e0e0e0" stroke-width="2"/><path d="M67 62l6-4 6 10-4 4c2 5 6 9 11 11l4-4 10 6-4 6c-14 2-31-15-29-29z" fill="none" stroke="#c4111b" stroke-width="3" stroke-linejoin="round"/></svg>
    <h5>PHONE NUMBER</h5>
    <p style="font-size:20px">0771 555 0192</p>
  </div>
  <div class="c-item" style="left:722px">
    <svg width="150" height="150" viewBox="0 0 150 150"><path d="M20 90 A58 58 0 0 1 130 50 A52 52 0 0 0 20 90Z" fill="var(--red)"/><circle cx="80" cy="78" r="56" fill="#fff"/><circle cx="80" cy="78" r="44" fill="none" stroke="#e0e0e0" stroke-width="2"/><rect x="58" y="64" width="44" height="30" fill="none" stroke="#c4111b" stroke-width="3"/><path d="M58 64l22 18 22-18M58 94l16-14M102 94L86 80" fill="none" stroke="#c4111b" stroke-width="3"/></svg>
    <h5>EMAIL ADDRESS</h5>
    <p>sales@brentavel.co.uk</p>
  </div>
</section>

<!-- appointment -->
<svg class="abs" style="left:0;top:3720px" width="1200" height="140" viewBox="0 0 1200 140">
  <path d="M0 140 L0 120 C400 130 800 60 1200 60 L1200 140 Z" fill="#fff"/>
  <path d="M420 112 C700 60 950 20 1200 20 L1200 60 C950 50 700 80 420 112 Z" fill="var(--red)"/>
</svg>
<h2 class="abs appt-title">MAKE AN APPOINTMENT</h2>
<div class="abs appt-addr">BRENTAVEL BODYSHOP, HARROWGATE TRADE PARK,<br>COPSE LANE, ELMSWORTH, DERBYSHIRE, DE99 4ZQ</div>
<div class="abs field" style="left:275px;top:3991px;width:317px">Date</div>
<div class="abs field" style="left:604px;top:3991px;width:319px">Time</div>
<div class="abs field" style="left:275px;top:4056px;width:648px">Price</div>
<div class="abs appt-note">If you are unable to keep your appointment,<br>Please contact us as soon as possible</div>

<!-- footer -->
<div class="abs footer-bg"></div>
<svg class="abs" style="left:0;top:4240px" width="1200" height="130" viewBox="0 0 1200 130">
  <path d="M0 30 C300 90 600 60 840 20 C600 80 300 120 0 110 Z" fill="var(--red)"/>
  <path d="M0 110 C300 120 600 80 840 20 C900 40 1100 55 1200 60 L1200 60 L1200 60 C900 70 600 95 0 128 Z" fill="#fff" opacity="0"/>
</svg>
<nav class="abs foot-nav"><span>HOME</span><span>ABOUT US</span><span>SERVICE</span><span>CUSTOM</span><span>GALLERY</span><span>CONTACT</span></nav>
<div class="abs copy">© 2019 Company Name &nbsp;All right reserved</div>
<span class="abs social" style="left:804px"></span>
<span class="abs social" style="left:850px"></span>
<span class="abs social" style="left:894px"></span>
<span class="abs social" style="left:939px"></span>
<div class="abs pay">QUIDLOOP</div>

</body>
</html>
```